New Chiropractic Office needs a fresh flyer design!

We need a flyer design for our chiropractic office for our hometown based chiropractic office called "Corvale Chiropractic" Dr. Martin Corvale provides chiropractic services including adjustments, xrays and wellness exercises with a fresh approach to chiropractic which focuses on getting your body aligned correctly to be a better you. We dont like to focus on coming in just for pain although that is what most people associate our operation with so we understand that comes with the territory. However we would like our flyers to express health and wellness rather than medical or pain. We would like our flyer to emphasize our "New Patient Special" which includes consultation, exam, xrays and first treatment for only $50. We also accept most insurance plans. Call for an appointment 618-390-2757.

Industry/Entity Type

Office

```html
<!DOCTYPE html>
<html lang="en">
<head>
<meta charset="utf-8">
<title>Corvale Chiropractic – New Patient Special</title>
<link href="https://fonts.googleapis.com/css2?family=Crimson+Text:wght@400;600&display=swap" rel="stylesheet">
<style>
  :root {
    --paper: #ffffff;
    --green-deep: #37593c;
    --green-mid: #4d7752;
    --green-light: #5f8a62;
    --green-glow: rgba(140, 180, 135, 0.35);
    --lime: #a3c94a;
    --olive: #7e9a3a;
    --ink: #1d1d1d;
    --text-light: #f4f6f1;
  }
  * { box-sizing: border-box; margin: 0; padding: 0; }
  html, body { width: 872px; height: 1200px; overflow: hidden; background: var(--paper); }
  .flyer {
    position: relative;
    width: 872px;
    height: 1200px;
    font-family: "Crimson Text", Georgia, serif;
    background: var(--paper);
  }

  /* Header */
  .masthead {
    position: absolute; top: 0; left: 0; width: 872px; height: 156px;
    display: flex; flex-direction: column; align-items: center; justify-content: center; gap: 10px;
  }
  .masthead__dot { width: 52px; height: 52px; border-radius: 50%; background: var(--olive); }
  .masthead__name {
    font-size: 23px; font-weight: 600; letter-spacing: 1.5px; color: var(--green-deep);
    text-transform: uppercase;
  }

  /* Offer panel */
  .offer {
    position: absolute; top: 156px; left: 0; width: 872px; height: 728px;
    background: linear-gradient(160deg, var(--green-light) 0%, var(--green-mid) 45%, var(--green-deep) 100%);
    overflow: hidden;
  }
  .offer__figure {
    position: absolute; left: 0; top: 0; width: 560px; height: 728px;
    background: radial-gradient(ellipse 280px 460px at 240px 330px, var(--green-glow), rgba(140,180,135,0) 100%);
  }
  .offer__lower-band {
    position: absolute; left: 0; top: 445px; width: 872px; height: 283px;
    background: rgba(255,255,255,0.04);
  }
  .offer__badge {
    position: absolute; left: 57px; top: 73px; width: 194px; height: 190px;
    border-radius: 46%;
    background: linear-gradient(180deg, #6f8fb0 0%, #8aa07a 55%, #b0734f 100%);
    border: 3px solid rgba(255,255,255,0.85);
  }
  .offer__copy {
    position: absolute; right: 46px; top: 60px; width: 560px; text-align: right; color: var(--text-light);
  }
  .offer__title { font-size: 57px; font-weight: 400; line-height: 1.1; }
  .offer__details { margin-top: 22px; font-size: 28px; line-height: 1.75; }
  .offer__price { color: var(--lime); font-size: 44px; line-height: 1; }
  .offer__call {
    position: absolute; right: 46px; top: 478px; text-align: right; color: var(--text-light);
  }
  .offer__call-lead { font-size: 49px; line-height: 1.2; }
  .offer__phone { font-size: 60px; color: var(--lime); line-height: 1.2; letter-spacing: 1px; }

  /* Photo strip */
  .activity-strip {
    position: absolute; top: 884px; left: 0; width: 872px; height: 170px; display: flex;
  }
  .activity-strip__tile { flex: 1; height: 100%; }
  .tile--mat { background: linear-gradient(180deg, #9a9aa0 0%, #5a4f8a 60%, #3c3f6e 100%); }
  .tile--trail { background: linear-gradient(160deg, #e39a4a 0%, #b35a2e 55%, #6b3a2a 100%); }
  .tile--shoe { background: linear-gradient(160deg, #cfd4da 0%, #d98aa0 55%, #8a6a5a 100%); }
  .tile--core { background: linear-gradient(180deg, #2a2a2a 0%, #b07a56 35%, #8c5b3c 100%); }
  .tile--track { background: linear-gradient(180deg, #4d6a8a 0%, #8c3a32 60%, #b04a3a 100%); }

  /* Footer */
  .footer {
    position: absolute; top: 1054px; left: 0; width: 872px; height: 146px;
    display: flex; flex-direction: column; align-items: center; justify-content: center; gap: 2px;
  }
  .footer__lead { font-size: 26px; color: var(--olive); }
  .footer__url { font-size: 48px; color: var(--ink); line-height: 1.1; }
</style>
</head>
<body>
<div class="flyer">
  <header class="masthead">
    <span class="masthead__dot"></span>
    <span class="masthead__name">Corvale Chiropractic</span>
  </header>

  <section class="offer">
    <div class="offer__figure" role="img" aria-label="Soft green illustration of a person's back with a hand resting on the lower spine"></div>
    <div class="offer__lower-band"></div>
    <div class="offer__badge" role="img" aria-label="Photo of a sprinter launching from the blocks on a running track"></div>

    <div class="offer__copy">
      <h1 class="offer__title">New Patient Special</h1>
      <p class="offer__details">which includes consultation, exam, xrays<br>and first treatment for only <span class="offer__price">$50</span>. We also<br>accept most insurance plans.</p>
    </div>

    <div class="offer__call">
      <p class="offer__call-lead">Call for an appointment</p>
      <p class="offer__phone">618-390-2757.</p>
    </div>
  </section>

  <div class="activity-strip">
    <div class="activity-strip__tile tile--mat" role="img" aria-label="Photo of a woman stretching on a purple exercise mat"></div>
    <div class="activity-strip__tile tile--trail" role="img" aria-label="Photo of running shoes on a sunlit dirt trail"></div>
    <div class="activity-strip__tile tile--shoe" role="img" aria-label="Close-up photo of a pink running shoe in stride"></div>
    <div class="activity-strip__tile tile--core" role="img" aria-label="Photo of a toned athletic midsection"></div>
    <div class="activity-strip__tile tile--track" role="img" aria-label="Photo of a runner's legs in starting blocks on a track"></div>
  </div>

  <footer class="footer">
    <p class="footer__lead">more info? visit our website.</p>
    <p class="footer__url">corvalechiropractic.com</p>
  </footer>
</div>
</body>
</html>
```